Business Card for Willowcrest Terrain Advisors

We need a business card for Willowcrest Terrain Advisors. The company website address is provided below. The company logo is attached. We provide specialized permafrost services to the mining, transportation, and oil & gas industries. The card should be prepared for:
Dominic Halloway, PhD.
Willowcrest Terrain Advisors
PO Box 418529
Birch Hollow, Alaska 99612
Direct: +1-907-555-2964
Email: dhalloway@terrainadvisors-example.com
Website: www.willowcrestterrainadvisors-example.com

```html
<!DOCTYPE html>
<html lang="en">
<head>
<meta charset="UTF-8">
<title>Willowcrest Terrain Advisors — Business Card</title>
<link rel="stylesheet" href="https://fonts.googleapis.com/css2?family=Montserrat:wght@400;600;700&display=swap">
<style>
  :root {
    --backdrop: #8a7458;
    --card: #ffffff;
    --ink: #161b22;
    --ink-soft: #2a2f36;
  }
  * { margin: 0; padding: 0; box-sizing: border-box; }
  html, body {
    width: 900px; height: 1200px; overflow: hidden;
    background: var(--backdrop);
    font-family: "Montserrat", sans-serif;
    color: var(--ink);
  }
  .canvas { position: relative; width: 900px; height: 1200px; }
  .card {
    position: absolute; left: 80px; width: 742px; height: 440px;
    background: var(--card); border-radius: 40px;
  }
  .card--front { top: 132px; }
  .card--back { top: 638px; }

  .wordmark {
    position: absolute; font-weight: 600; color: var(--ink);
    text-transform: uppercase; white-space: nowrap;
  }
  .card--front .wordmark { left: 45px; top: 82px; font-size: 22px; letter-spacing: 3px; }
  .card--back .wordmark {
    left: 0; right: 0; top: 200px; text-align: center;
    font-size: 28px; letter-spacing: 3.5px;
  }

  .holder { position: absolute; left: 38px; top: 266px; }
  .holder__name { font-size: 26px; font-weight: 700; line-height: 1.1; }
  .holder__role { font-size: 16px; font-weight: 400; color: var(--ink-soft); margin-top: 2px; }

  .rule {
    position: absolute; left: 38px; top: 326px; width: 670px; height: 1.5px;
    background: var(--ink);
  }

  .contacts { position: absolute; left: 38px; top: 343px; list-style: none; }
  .contacts li {
    display: flex; align-items: center; height: 22px;
    font-size: 15px; color: var(--ink-soft);
  }
  .contacts svg { width: 13px; height: 13px; margin-right: 14px; flex: none; fill: var(--ink); }

  .address {
    position: absolute; left: 468px; top: 372px;
    border-left: 1.5px solid var(--ink); padding-left: 18px;
    font-size: 16px; line-height: 21px; color: var(--ink-soft);
  }
</style>
</head>
<body>
<main class="canvas">
  <section class="card card--front">
    <div class="wordmark">Willowcrest Terrain Advisors</div>

    <div class="holder">
      <div class="holder__name">Dominic Halloway, PhD.</div>
      <div class="holder__role">CEO &amp; Founder</div>
    </div>

    <div class="rule"></div>

    <ul class="contacts">
      <li>
        <svg viewBox="0 0 16 16" aria-hidden="true"><path d="M2 5c0-2 3-3 6-3s6 1 6 3v1.5h-3V5H5v1.5H2z M4 8h8l2 6H2z M8 9.5a1.8 1.8 0 1 0 0 3.6a1.8 1.8 0 1 0 0-3.6z"/></svg>
        +1-907-555-2964
      </li>
      <li>
        <svg viewBox="0 0 16 16" aria-hidden="true"><path d="M1 3h14v1.2L8 9 1 4.2z M1 6l7 4.8L15 6v7H1z"/></svg>
        dhalloway@terrainadvisors-example.com
      </li>
      <li>
        <svg viewBox="0 0 16 16" aria-hidden="true"><path d="M8 1a7 7 0 1 0 0 14A7 7 0 1 0 8 1z M4 4.5l2.5-.5 1 2-2 1.5 1 2.5-1.5 1.5L3 8.5z M9.5 3l2.5 1.5-.5 2-2 .5z M10 9l2.5 0-1 3-2 .5z" fill-rule="evenodd"/></svg>
        www.willowcrestterrainadvisors-example.com
      </li>
    </ul>

    <address class="address" style="font-style: normal;">
      PO Box 418529<br>
      Birch Hollow, Alaska 99612
    </address>
  </section>

  <section class="card card--back">
    <div class="wordmark">Willowcrest Terrain Advisors</div>
  </section>
</main>
</body>
</html>
```